Book Cover needed - Disinformation and fake news

I need a book cover (front, back, spine) for the 1st edition of a book entitled ‘Marea Silenciosa’ (Means – Silent Tide) and subtitled ‘Los ecos que nadie quiso escuchar’ (Means - The echoes nobody wanted to hear) (inverted commas not to be part of the title and subtitle). The author is ‘Tomás Herreruela’. The finished size of the paperback version will be 5.25" x 8". There will be paperback and e-book versions, so 2 covers will need to be provided: one for the e-book version just with the front cover, and the full book cover for the paperback version.
The final number of pages is expected to be in the region of 350-500 pages. Text for the back cover is down below, and at the bottom of the back cover should have space for the ISBN bar code on the right. The books will be published with PQN - Velmora, so should follow their indications for any specification needed.
The topics discussed include disinformation, fake news, psychological operations. Feel free to design the cover based on those. The design should be original and not include any stock images that have been created by someone else or may require obtaining a copyright license to use.
Back Cover Text (spacing should be respected) :
Oficina del consenso, desinformación, “fake news”... en los últimos años nos hemos visto envueltos en una discusión pública rodeados de estos términos sin terminar de entender exactamente qué significan y lo que es peor, sin saber que realmente nos rodean desde que el hombre es hombre.
En esta obra el autor busca acercanos al mundo de la Marea Silenciosa, aquellas operaciones que buscan influir sobre el comportamiento de la población. Sin hacer uso de un lenguaje excesivamente técnico relata como la evolución de la naturaleza de la guerra a los parámetros del siglo XXI promueve un enfoque del conflicto que no supone un uso de la fuerza tradicional. ¿Para qué atacar las instituciones de un país de forma directa, cuando puedes fomentar el conflicto social entre grupos antagónicos y desestabilizar sin realizar un solo disparo?
¿Cómo razona el ser humano? ¿Son nuestras ideas tan nuestras como creemos? ¿Por qué importa tanto el uso preciso del lenguaje a la hora de comunicarnos?, ¿Cómo nos afectan las razones y emociones de los demás? ¿Por qué tendemos a prestar mayor atención a argumentos que encajen con nuestras propias ideas? ¿Cómo nos afecta la conversación en redes sociales?
Armados con el conocimiento que reside en este libro, quizás, seamos menos susceptibles de caer bajo la influencia de grupos con intereses espurios.
General public with an interest on disinformation - fake news

```html
<!DOCTYPE html>
<html lang="es">
<head>
<meta charset="utf-8">
<title>Marea Silenciosa — Cubierta completa</title>
<link rel="stylesheet" href="https://fonts.googleapis.com/css2?family=Montserrat:wght@500;600;700&family=Cormorant+Garamond:wght@500&display=swap">
<style>
  :root {
    --backdrop: #333333;
    --navy: #0e2647;
    --navy-deep: #0a1538;
    --red: #c9432f;
    --white: #f2f2f2;
    --black: #000000;
    --rule: #b23a2c;
  }
  * { box-sizing: border-box; margin: 0; padding: 0; }
  html, body {
    width: 850px; height: 1200px; overflow: hidden;
    background: var(--backdrop);
    font-family: "Montserrat", sans-serif;
  }
  .wrap {
    position: absolute; left: 24px; top: 311px;
    width: 802px; height: 577px;
    display: flex;
  }
  /* Back cover */
  .back {
    position: relative; width: 379px; height: 100%;
    background: linear-gradient(180deg, var(--navy) 0%, var(--navy-deep) 100%);
    overflow: hidden;
  }
  .back-art {
    position: absolute; left: 0; top: 250px; width: 379px; height: 327px;
    background: radial-gradient(ellipse at 45% 40%, rgba(40,80,140,0.35) 0%, rgba(20,40,90,0.15) 45%, rgba(0,0,0,0) 70%);
  }
  .back-title {
    position: absolute; left: 31px; top: 33px; width: 318px;
    font-weight: 700; font-size: 17.5px; letter-spacing: 0.16em;
    color: var(--white); white-space: nowrap;
  }
  .back-title .accent { color: var(--red); letter-spacing: 0.3em; margin-right: 6px; }
  .back-subtitle {
    position: absolute; left: 31px; top: 60px; width: 318px;
    font-weight: 700; font-size: 9.4px; letter-spacing: 0.09em;
    color: var(--white); white-space: nowrap;
  }
  .rule {
    position: absolute; left: 31px; width: 318px; height: 0;
    border-top: 0.8px solid var(--rule);
  }
  .rule.top { top: 94px; }
  .rule.bottom { top: 438px; }
  .blurb {
    position: absolute; left: 31px; top: 116px; width: 318px;
    color: var(--white); font-weight: 500;
    font-size: 8.4px; line-height: 10.7px; letter-spacing: 0.05em;
    text-align: justify;
  }
  .blurb p + p { margin-top: 10.7px; }
  .barcode-area {
    position: absolute; left: 226px; top: 477px; width: 122px; height: 69px;
    background: #ffffff;
    display: flex; align-items: center; justify-content: center;
    font-family: "Cormorant Garamond", serif; font-size: 6.5px;
    letter-spacing: 0.3em; color: #222;
  }
  /* Spine */
  .spine {
    position: relative; width: 44px; height: 100%;
    background: var(--red);
  }
  .spine-author, .spine-title {
    position: absolute; left: 0; width: 44px;
    writing-mode: vertical-rl;
    display: flex; align-items: center;
    color: var(--navy); font-weight: 600;
  }
  .spine-author { top: 30px; height: 160px; font-size: 10.5px; letter-spacing: 0.12em; }
  .spine-title { top: 312px; height: 240px; font-size: 12.5px; letter-spacing: 0.28em; font-weight: 700; }
  .spine-art {
    position: absolute; left: 0; top: 219px; width: 44px; height: 62px;
    background: radial-gradient(ellipse at 50% 60%, #1c3866 0%, #0a1530 45%, #000 80%);
  }
  /* Front cover */
  .front {
    position: relative; width: 379px; height: 100%;
    background: var(--navy);
  }
  .front-title-top, .front-title-main {
    position: absolute; left: 0; width: 379px; text-align: center;
    font-weight: 700; white-space: nowrap;
  }
  .front-title-top {
    top: 20px; color: var(--red);
    font-size: 36px; letter-spacing: 0.42em; text-indent: 0.42em;
  }
  .front-title-main {
    top: 66px; color: var(--white);
    font-size: 35px; letter-spacing: 0.11em; text-indent: 0.11em;
  }
  .front-art {
    position: absolute; left: 71px; top: 147px; width: 236px; height: 324px;
    border: 0.8px solid var(--rule);
    background: radial-gradient(ellipse at 48% 58%, #1d3a68 0%, #0b1a3a 35%, #000 65%);
  }
  .front-subtitle {
    position: absolute; left: 0; top: 515px; width: 379px; text-align: center;
    color: var(--white); font-weight: 700; font-size: 9.4px; letter-spacing: 0.09em;
    white-space: nowrap;
  }
  .author-band {
    position: absolute; left: 0; bottom: 0; width: 379px; height: 38px;
    background: var(--black);
    display: flex; align-items: center; justify-content: center;
    color: var(--red); font-weight: 700; font-size: 16px;
    letter-spacing: 0.38em; text-indent: 0.38em; white-space: nowrap;
  }
</style>
</head>
<body>
  <div class="wrap">
    <section class="back">
      <div class="back-art" role="img" aria-label="Rostro azul difuminado como fondo de la contracubierta"></div>
      <h2 class="back-title"><span class="accent">MAREA</span> SILENCIOSA</h2>
      <p class="back-subtitle">LOS ECOS QUE NADIE QUISO ESCUCHAR</p>
      <div class="rule top"></div>
      <div class="blurb">
        <p>Oficina del consenso, desinformación, “fake news”... en los últimos años nos hemos visto envueltos en una discusión pública rodeados de estos términos sin terminar de entender exactamente qué significan y lo que es peor, sin saber que realmente nos rodean desde que el hombre es hombre.</p>
        <p>En esta obra el autor busca acercanos al mundo de la Marea Silenciosa, aquellas operaciones que buscan influir sobre el comportamiento de la población. Sin hacer uso de un lenguaje excesivamente técnico relata como la evolución de la naturaleza de la guerra a los parámetros del siglo XXI promueve un enfoque del conflicto que no supone un uso de la fuerza tradicional. ¿Para qué atacar las instituciones de un país de forma directa, cuando puedes fomentar el conflicto social entre grupos antagónicos y desestabilizar sin realizar un solo disparo?</p>
        <p>¿Cómo razona el ser humano? ¿Son nuestras ideas tan nuestras como creemos? ¿Por qué importa tanto el uso preciso del lenguaje a la hora de comunicarnos?, ¿Cómo nos afectan las razones y emociones de los demás? ¿Por qué tendemos a prestar mayor atención a argumentos que encajen con nuestras propias ideas? ¿Cómo nos afecta la conversación en redes sociales?</p>
        <p>Armados con el conocimiento que reside en este libro, quizás, seamos menos susceptibles de caer bajo la influencia de grupos con intereses espurios.</p>
      </div>
      <div class="rule bottom"></div>
      <div class="barcode-area">BARCODE AREA</div>
    </section>

    <section class="spine">
      <div class="spine-author">TOMÁS HERRERUELA</div>
      <div class="spine-art" role="img" aria-label="Miniatura de la ilustración de portada"></div>
      <div class="spine-title">MAREA SILENCIOSA</div>
    </section>

    <section class="front">
      <h1 class="front-title-top">MAREA</h1>
      <h1 class="front-title-main">SILENCIOSA</h1>
      <div class="front-art" role="img" aria-label="Ilustración: cabeza azul abierta con un tablero de ajedrez y sus piezas en su interior, sobre fondo negro"></div>
      <p class="front-subtitle">LOS ECOS QUE NADIE QUISO ESCUCHAR</p>
      <div class="author-band">TOMÁS HERRERUELA</div>
    </section>
  </div>
</body>
</html>
```